Lumoxra - Web Design Project

I am looking for a 5 page design.
I would like it to be like the design of this site: www.quarvelle.com.
Which means it can be all one page effectively. With quick scroll tabs at the top.
I would like it to include parallax scrolling (The parallax effect uses multiple backgrounds which seem to move at different speeds to create a sensation of depth (creating a faux-3D effect)).
I have uploaded my logo. I would like this to be used in the site design.
I would like the site design to include 3D DNA creative.
Please note the PixHaven photos attached do not belong to me they are purely to inspire creative ideas. However I would be more than happy to purchase these photos to use if the designer thought this would be beneficial.
Must have
- parallax scrolling
DNA pictures (3D effect)
Please use site for reference: www.quarvelle.com
Use at least 1 of the logos in design...

```html
<!DOCTYPE html>
<html lang="en">
<head>
<meta charset="utf-8">
<title>Lumoxra – DNA Research</title>
<link rel="stylesheet" href="https://fonts.googleapis.com/css2?family=Questrial&family=Source+Sans+3:wght@400;600;700&display=swap">
<style>
  :root{
    --navy:#1f3f73;
    --ink:#12305f;
    --text:#4a5566;
    --muted:#7a8596;
    --orange:#f58a12;
    --orange-dark:#e06e00;
    --header-bg:#f2f6fb;
    --band-top:#1f5d96;
    --band-bottom:#0f3a6b;
    --footer-bg:#eef3f9;
    --white:#ffffff;
  }
  *{margin:0;padding:0;box-sizing:border-box}
  html,body{width:1200px;height:2317px;overflow:hidden}
  body{position:relative;background:var(--white);font-family:"Source Sans 3",sans-serif;color:var(--text)}
  .abs{position:absolute}

  /* header */
  .site-header{left:0;top:0;width:1200px;height:157px;background:linear-gradient(#fff,var(--header-bg))}
  .brand{left:140px;top:66px;font-family:"Questrial",sans-serif;font-size:38px;letter-spacing:9px;color:var(--navy)}
  .main-nav{left:528px;top:86px;display:flex;font-family:"Questrial",sans-serif;font-size:18px;color:var(--ink)}
  .main-nav a{color:inherit;text-decoration:none;padding:0 16px;border-left:1px solid #b9c4d4;line-height:24px}
  .main-nav a:first-child{border-left:none;padding-left:0}

  /* hero */
  .hero{left:0;top:157px;width:1200px;height:607px;background:radial-gradient(ellipse at 68% 45%,#1f8fd6 0%,#0b4a7c 30%,#06223d 62%,#04152a 100%)}
  .hero-kicker{left:76px;top:308px;font-size:42px;color:var(--white);font-weight:400}
  .hero-title{left:74px;top:354px;font-size:58px;font-weight:700;color:var(--white);letter-spacing:0.5px}
  .hero-text{left:76px;top:427px;width:450px;font-size:16.5px;line-height:25px;color:#c9d7e6}
  .hero-dots{left:541px;top:737px;display:flex;gap:5px}
  .hero-dots span{width:12px;height:12px;border-radius:50%;background:#7f8792}
  .hero-dots span:first-child{background:#7cc8f4}

  /* about */
  .about-art{left:88px;top:812px;width:322px;height:284px;background:radial-gradient(circle,#3b3fd0 0%,#5a6fe0 35%,rgba(255,255,255,0) 70%)}
  .section-title{font-size:34px;font-weight:400;color:var(--navy)}
  .about-title{left:443px;top:806px}
  .lead{font-size:19.5px;font-weight:600;color:var(--ink)}
  .about-lead{left:444px;top:860px}
  .copy{font-size:13.8px;line-height:27px;color:var(--text)}
  .about-copy{left:444px;top:894px;width:695px}
  .btn{display:inline-block;background:linear-gradient(var(--orange),var(--orange-dark));color:var(--white);font-size:13.5px;padding:0 12px;height:31px;line-height:31px;border-radius:2px;text-decoration:none}
  .btn::after{content:" \203A"}
  .about-btn{left:442px;top:1051px}

  /* features */
  .features{left:0;top:1133px;width:1200px;height:588px;background:linear-gradient(#f4f7fb,#fff 25%)}
  .feature-photo{width:506px;height:223px;border:5px solid #fff;box-shadow:0 0 0 1px #d9dee6}
  .photo-lab{left:65px;top:1242px;background:linear-gradient(90deg,#8a8f99,#d7d9dc 45%,#6db4e6)}
  .photo-screen{left:628px;top:1242px;background:linear-gradient(90deg,#b7d6f2,#0d2a48 40%,#1b6fae 70%,#dbeaf8)}
  .feature-title-left{left:65px;top:1179px}
  .feature-title-right{left:629px;top:1182px}
  .feat-lead{font-size:17px;font-weight:600;color:var(--ink)}
  .feat-copy{font-size:13.8px;line-height:27px;width:510px}
  .feat-copy p+p{margin-top:5px}
  .btn-left{left:65px;top:1644px}
  .btn-right{left:628px;top:1644px}

  /* services band */
  .services{left:0;top:1721px;width:1200px;height:436px;background:linear-gradient(var(--band-top),var(--band-bottom))}
  .services-title{left:65px;top:1759px;font-size:32px;color:var(--white)}
  .service-photo{top:1819px;width:312px;height:136px;border:4px solid #fff}
  .svc-title{top:1973px;font-size:19px;color:var(--white)}
  .svc-copy{top:2003px;width:310px;font-size:13.8px;line-height:24px;color:#b9cde3}
  .svc-more{top:2085px;font-size:13px;font-weight:700;color:var(--white);text-decoration:none}
  .svc-more::after{content:" \203A"}

  /* footer */
  .site-footer{left:0;top:2157px;width:1200px;height:160px;background:var(--footer-bg)}
  .footer-nav{left:52px;top:2202px;font-size:14.5px;color:var(--ink);display:flex}
  .footer-nav a{color:inherit;text-decoration:none;padding:0 9px;border-left:1px solid var(--ink);line-height:14px}
  .footer-nav a:first-child{border-left:none;padding-left:0}
  .copyright{left:52px;top:2239px;font-size:12.5px;color:var(--muted)}
  .social{left:1007px;top:2195px;display:flex;gap:9px}
  .social span{width:34px;height:34px;border-radius:50%;background:#1f3f73}
</style>
</head>
<body>
  <header class="site-header abs">
    <div class="brand abs">LUMOXRA</div>
    <nav class="main-nav abs">
      <a href="#">MAIN</a><a href="#">ABOUT US</a><a href="#">SERVICES</a><a href="#">RESEARCH</a><a href="#">BLOG</a><a href="#">CONTACT</a>
    </nav>
  </header>

  <section class="hero abs" role="img" aria-label="Glowing blue 3D DNA double helix on a dark background"></section>
  <h2 class="hero-kicker abs">Mauris vitae felis vestibulum</h2>
  <h1 class="hero-title abs">DNA RESEARCH</h1>
  <p class="hero-text abs">Ut ante enim, dapibus malesuada, fringilla eu, condimentum quis, tellus. Aenean porttitor eros vel dolor. Donec convallis pede venenatis nibh. Duis quam.</p>
  <div class="hero-dots abs"><span></span><span></span><span></span><span></span></div>

  <div class="about-art abs" role="img" aria-label="Blue 3D molecule model with green bonds"></div>
  <h2 class="section-title about-title abs">About Lumoxra Research</h2>
  <p class="lead about-lead abs">Phasellus felis dolor, scelerisque a, tempus eget, lobortis id, libero.</p>
  <p class="copy about-copy abs">Donec scelerisque leo ac risus. Praesent sit amet est. In dictum, dolor eu dictum porttitor, enim felis viverra mi, eget luctus massa purus quis odio. Etiam nulla massa, pharetra facilisis, volutpat in, imperdiet sit amet, sem. Aliquam nec erat at purus cursus interdum. Vestibulum ligula augue, bibendum accumsan, vestibulum ut, commodo a, mi. Morbi ornare gravida elit. Integer congue, augue et malesuada iaculis, ipsum dui aliquet felis, at cursus magna nisl nec elit. Donec iaculis diam a nisi accumsan viverra.</p>
  <a class="btn about-btn abs" href="#">Learn More</a>

  <section class="features abs"></section>
  <h2 class="section-title feature-title-left abs">What We Do</h2>
  <h2 class="section-title feature-title-right abs">Analysis &amp; Treatment</h2>
  <div class="feature-photo photo-lab abs" role="img" aria-label="Two scientists in a laboratory examining samples"></div>
  <div class="feature-photo photo-screen abs" role="img" aria-label="Hand touching a screen showing a DNA model"></div>

  <div class="abs" style="left:65px;top:1484px">
    <p class="feat-lead">Maecenas aliquet velit vel turpis</p>
    <div class="copy feat-copy" style="margin-top:9px">
      <p>Donec scelerisque leo ac risus. Praesent sit amet est. In dictum, dolor eu dictum porttitor, enim felis viverra mi, eget luctus massa purus quis odio.</p>
      <p>Etiam nulla massa, pharetra facilisis, volutpat in, imperdiet sit amet, sem. Aliquam nec erat at purus cursus interdum. Vestibulum ligula augue.</p>
    </div>
  </div>
  <div class="abs" style="left:628px;top:1484px">
    <p class="feat-lead">Phasellus felis dolor, scelerisque a, tempus</p>
    <div class="copy feat-copy" style="margin-top:9px">
      <p>Donec scelerisque leo ac risus. Praesent sit amet est. In dictum, dolor eu dictum porttitor, enim felis viverra mi, eget luctus massa purus quis odio. Etiam nulla massa, pharetra facilisis, volutpat in, imperdiet sit amet, sem. Aliquam nec erat at purus cursus interdum.</p>
    </div>
  </div>
  <a class="btn btn-left abs" href="#">Learn More</a>
  <a class="btn btn-right abs" href="#">Learn More</a>

  <section class="services abs" role="img" aria-label="Deep blue band with a faint DNA helix"></section>
  <h2 class="services-title abs">Services We Provide</h2>

  <div class="service-photo abs" style="left:66px;background:linear-gradient(90deg,#e9eef5,#5f8fd6 50%,#e9eef5)" role="img" aria-label="Colourful 3D DNA strand"></div>
  <div class="service-photo abs" style="left:444px;background:linear-gradient(90deg,#dce8f5,#9bbde0 40%,#f2f5f9)" role="img" aria-label="Scientist holding a test tube beside a DNA model"></div>
  <div class="service-photo abs" style="left:821px;background:linear-gradient(90deg,#3a8fd8,#e8eef5 50%,#9fb5cc)" role="img" aria-label="Researcher using a microscope"></div>

  <h3 class="svc-title abs" style="left:69px">Etiam est nunc venenatis</h3>
  <h3 class="svc-title abs" style="left:448px">Etiam est nunc venenatis</h3>
  <h3 class="svc-title abs" style="left:825px">Etiam est nunc venenatis</h3>
  <p class="svc-copy abs" style="left:69px">Phasellus felis dolor, scelerisque a, tempus eget, lobortis id, libero. Donec scelerisque leo ac risus. Praesent sit amet est.</p>
  <p class="svc-copy abs" style="left:448px">Phasellus felis dolor, scelerisque a, tempus eget, lobortis id, libero. Donec scelerisque leo ac risus. Praesent sit amet est</p>
  <p class="svc-copy abs" style="left:825px">Phasellus felis dolor, scelerisque a, tempus eget, lobortis id, libero. Donec scelerisque leo ac risus. Praesent sit amet est.</p>
  <a class="svc-more abs" href="#" style="left:70px">LEARN MORE</a>
  <a class="svc-more abs" href="#" style="left:449px">LEARN MORE</a>
  <a class="svc-more abs" href="#" style="left:826px">LEARN MORE</a>

  <footer class="site-footer abs"></footer>
  <nav class="footer-nav abs">
    <a href="#">MAIN</a><a href="#">ABOUT US</a><a href="#">SERVICES</a><a href="#">RESEARCH</a><a href="#">BLOG</a><a href="#">CONTACT</a>
  </nav>
  <p class="copyright abs">© 2013 Company Name.&nbsp; All right reserved.&nbsp; Term of Use</p>
  <div class="social abs" aria-label="Social links"><span></span><span></span><span></span><span></span></div>
</body>
</html>
```